Postcard Design

I'm a licensed REALTORĀ® with Homestead Partners in East Tennessee specializing in residential real estate. I want to design a postcard that I can send to potential clients like for sale by owners and expired listings. I originally wanted to design 2 cards, but everything would be almost exact except for 1-2 sentences. I want to pinpoint my attributes and have a postcard that will catch client's eyes. I am applying my business logo and my profile picture. I am waiting on an updated photo from the photographer that I would prefer to use instead, but I also wanted to get started on this project.

Target Market(s)

For sale by owners and expired listings

Industry/Entity Type

Residential

Requirements
Must have
• I would like to point out why I would be a good candidate for these clients: Honesty and Integrity, Hard Working, Personal Attention to All Transactions, Extensive Market and Area Knowledge, Advertising and Marketing of the client's home.

```html
<!DOCTYPE html>
<html lang="en">
<head>
<meta charset="utf-8">
<title>Your Realtor for Life – Postcard</title>
<link rel="stylesheet" href="https://fonts.googleapis.com/css2?family=Cinzel:wght@400&family=Ubuntu:wght@400;500;700&display=swap">
<style>
  :root{
    --panel-top:#5a80b5;
    --panel-mid:#3f679f;
    --panel-deep:#2d5189;
    --band:#284a80;
    --white:#ffffff;
    --ink:#2b2b2b;
    --name:#3a3678;
    --rule:#2f5a8f;
    --badge:#243a66;
  }
  *{box-sizing:border-box;margin:0;padding:0}
  html,body{width:1200px;height:930px;overflow:hidden;background:var(--white)}
  body{position:relative;font-family:"Ubuntu",Arial,sans-serif;color:var(--ink)}
  .postcard{position:absolute;inset:0;width:1200px;height:930px;background:var(--white)}
  .hero{
    position:absolute;left:30px;top:30px;width:1140px;height:710px;
    background:radial-gradient(ellipse at 50% 0%,var(--panel-top) 0%,var(--panel-mid) 45%,var(--panel-deep) 100%);
    overflow:hidden;
  }
  .hero-waves{position:absolute;left:0;top:0;width:1140px;height:710px}
  .headline{
    position:absolute;left:0;top:44px;width:1140px;text-align:center;
    font-family:"Cinzel",Georgia,serif;font-size:67px;font-weight:400;color:var(--white);
    letter-spacing:1px;text-shadow:2px 3px 5px rgba(0,0,0,.45);line-height:1;
  }
  .gallery{position:absolute;top:138px;left:35px;display:flex;gap:36px}
  .gallery-photo{
    width:333px;height:218px;border:3px solid var(--white);border-radius:12px;
    box-shadow:0 3px 8px rgba(0,0,0,.35);
  }
  .photo-cabin{background:linear-gradient(180deg,#c9d8c2 0%,#6f8a55 45%,#5b4a36 70%,#6fa046 100%)}
  .photo-lake{background:linear-gradient(180deg,#3f5a2c 0%,#6d4a38 45%,#7f9f6a 65%,#5e7e8e 100%)}
  .photo-cottage{background:linear-gradient(180deg,#5c8fd6 0%,#b6d0ee 25%,#4d7a3a 50%,#b2322a 62%,#5f8f3a 100%)}
  .tagline-band{
    position:absolute;left:0;top:388px;width:1140px;height:58px;background:var(--band);
    display:flex;align-items:center;justify-content:center;
    font-weight:700;font-size:30px;letter-spacing:1.2px;color:var(--white);
    text-shadow:1px 2px 3px rgba(0,0,0,.4);
  }
  .why-title{
    position:absolute;left:92px;top:456px;font-size:24px;font-weight:700;color:var(--white);
    text-decoration:underline;text-underline-offset:4px;text-shadow:1px 2px 3px rgba(0,0,0,.4);
  }
  .reasons{position:absolute;left:272px;top:502px;list-style:none}
  .reasons li{
    display:flex;align-items:center;height:38px;font-size:23.5px;color:var(--white);
    letter-spacing:.3px;text-shadow:1px 2px 3px rgba(0,0,0,.4);
  }
  .reasons svg{width:30px;height:24px;margin-right:22px;flex:none}
  .brokerage{
    position:absolute;left:915px;top:570px;width:192px;height:106px;background:var(--badge);
    border:3px solid var(--white);border-radius:10px;box-shadow:0 3px 6px rgba(0,0,0,.4);
    display:flex;align-items:center;justify-content:center;text-align:center;
    font-weight:700;font-size:20px;line-height:1.15;color:var(--white);
  }
  .agent-photo{
    position:absolute;left:50px;top:622px;width:186px;height:246px;background:var(--white);
    padding:7px;box-shadow:1px 2px 6px rgba(0,0,0,.45);
  }
  .agent-photo div{width:100%;height:100%;background:linear-gradient(180deg,#3f6a2c 0%,#7c9a4a 40%,#c7a27c 75%,#e8ddd2 100%)}
  .agent-name{
    position:absolute;left:302px;top:757px;font-size:28px;font-weight:700;letter-spacing:2px;color:var(--name);
  }
  .contact{position:absolute;display:flex;align-items:center;font-size:23.5px;color:var(--ink);letter-spacing:.3px}
  .contact svg{width:22px;height:22px;margin-right:16px;flex:none}
  .contact-mobile{left:303px;top:807px}
  .contact-office{left:303px;top:848px}
  .contact-email{left:600px;top:805px}
  .contact-email svg{margin-right:20px}
  .contact-social{left:600px;top:848px}
  .social-square{width:22px;height:22px;background:var(--rule);margin-right:24px;flex:none}
  .footer-rule{position:absolute;left:30px;top:890px;width:1140px;height:9px;background:var(--rule)}
</style>
</head>
<body>
<div class="postcard">
  <section class="hero">
    <svg class="hero-waves" viewBox="0 0 1140 710" aria-hidden="true">
      <path d="M0 470 C300 520 600 560 1140 500 L1140 710 L0 710 Z" fill="rgba(255,255,255,.04)"/>
      <path d="M0 560 C350 500 700 640 1140 560" stroke="rgba(255,255,255,.12)" stroke-width="2" fill="none"/>
      <path d="M0 600 C380 540 760 680 1140 610" stroke="rgba(255,255,255,.10)" stroke-width="2" fill="none"/>
      <path d="M200 710 C500 640 800 690 1140 640 L1140 710 Z" fill="rgba(0,0,0,.08)"/>
    </svg>
    <h1 class="headline">YOUR REALTOR FOR LIFE!</h1>
    <div class="gallery">
      <div class="gallery-photo photo-cabin" role="img" aria-label="Historic log cabins on a green lawn with wooded hills behind"></div>
      <div class="gallery-photo photo-lake" role="img" aria-label="A-frame lake house with a dock on the water, surrounded by trees"></div>
      <div class="gallery-photo photo-cottage" role="img" aria-label="Red cottage with hedges and a garden under a blue sky"></div>
    </div>
    <p class="tagline-band">Licensed REALTOR® serving East Tennessee</p>
    <h2 class="why-title">Why choose Caroline Mercer?</h2>
    <ul class="reasons">
      <li><svg viewBox="0 0 30 24"><path d="M2 13 L10 21 L28 2" stroke="#fff" stroke-width="3" fill="none" stroke-linecap="round"/></svg>Honesty and Integrity</li>
      <li><svg viewBox="0 0 30 24"><path d="M2 13 L10 21 L28 2" stroke="#fff" stroke-width="3" fill="none" stroke-linecap="round"/></svg>Hard Working</li>
      <li><svg viewBox="0 0 30 24"><path d="M2 13 L10 21 L28 2" stroke="#fff" stroke-width="3" fill="none" stroke-linecap="round"/></svg>Personal Attention to All Transactions</li>
      <li><svg viewBox="0 0 30 24"><path d="M2 13 L10 21 L28 2" stroke="#fff" stroke-width="3" fill="none" stroke-linecap="round"/></svg>Extensive Market and Area Knowledge</li>
      <li><svg viewBox="0 0 30 24"><path d="M2 13 L10 21 L28 2" stroke="#fff" stroke-width="3" fill="none" stroke-linecap="round"/></svg>Advertising and Marketing of YOUR home</li>
    </ul>
    <div class="brokerage">Homestead<br>Partners</div>
  </section>

  <div class="agent-photo"><div role="img" aria-label="Portrait photo of the agent outdoors against green foliage"></div></div>
  <p class="agent-name">CAROLINE MERCER</p>

  <p class="contact contact-mobile">
    <svg viewBox="0 0 22 22"><rect x="5" y="1" width="12" height="20" rx="2" fill="#333"/><rect x="7" y="4" width="8" height="6" fill="#fff"/><g fill="#fff"><rect x="7" y="12" width="2" height="2"/><rect x="10" y="12" width="2" height="2"/><rect x="13" y="12" width="2" height="2"/><rect x="7" y="15" width="2" height="2"/><rect x="10" y="15" width="2" height="2"/><rect x="13" y="15" width="2" height="2"/></g></svg>
    865-555-0142
  </p>
  <p class="contact contact-office">
    <svg viewBox="0 0 22 22"><path d="M5 2 L9 2 L10 7 L7.5 9 C9 12.5 10.5 14 13 15 L15 12.5 L20 13.5 L20 17.5 C20 19 19 20 17.5 20 C9 19.5 2.5 13 2 4.5 C2 3 3 2 5 2 Z" fill="#333"/></svg>
    865-555-0187
  </p>
  <p class="contact contact-email">
    <svg viewBox="0 0 26 22"><rect x="1" y="4" width="24" height="15" fill="#333"/><path d="M1 4 L13 13 L25 4 M1 19 L10 11 M25 19 L16 11" stroke="#fff" stroke-width="1.6" fill="none"/></svg>
    cmercerhomes@example.com
  </p>
  <p class="contact contact-social"><span class="social-square"></span>http://www.connectpage.net/cmercerrealtor</p>

  <div class="footer-rule"></div>
</div>
</body>
</html>
```